Bravel Acres Business Cards

design business cards for our new business should match my Corvane Quotations business cards

Contact Information for Business Card

2817 W 68th N St
Tulsa, OK 74592

Requirements
Must have
• should match logo colors

```html
<!DOCTYPE html>
<html lang="en">
<head>
<meta charset="utf-8">
<title>Bravel Acres Business Cards</title>
<link rel="stylesheet" href="https://fonts.googleapis.com/css2?family=Montserrat:wght@400;500;700&display=swap">
<style>
  :root {
    --ink-deep: #012a2b;
    --leaf-green: #7bc043;
    --teal: #1fa9b4;
    --paper: #ffffff;
    --text-dark: #1d1d1d;
    --canvas: #ffffff;
  }
  * { margin: 0; padding: 0; box-sizing: border-box; }
  html, body { width: 800px; height: 1200px; overflow: hidden; background: var(--canvas); }
  body { font-family: "Montserrat", Arial, sans-serif; position: relative; }

  .card {
    position: absolute;
    left: 120px;
    width: 560px;
    height: 320px;
    overflow: hidden;
    box-shadow: 0 6px 18px rgba(0,0,0,0.12);
  }
  .card-front { top: 260px; background: var(--ink-deep); }
  .card-back { top: 620px; background: var(--paper); }

  .brand {
    position: absolute;
    display: flex;
    align-items: center;
    gap: 12px;
    color: var(--leaf-green);
    font-weight: 700;
    text-transform: uppercase;
    letter-spacing: 0.08em;
    white-space: nowrap;
  }
  .brand-dot { border-radius: 50%; background: var(--leaf-green); flex: none; }
  .card-front .brand { left: 50%; top: 50%; transform: translate(-50%, -50%); font-size: 40px; }
  .card-front .brand-dot { width: 22px; height: 22px; }

  .back-panel {
    position: absolute; left: 0; top: 0; width: 285px; height: 100%;
    background: var(--ink-deep);
  }
  .back-panel .brand { left: 50%; top: 50%; transform: translate(-50%, -50%); font-size: 22px; gap: 8px; }
  .back-panel .brand-dot { width: 13px; height: 13px; }
  .divider-rule {
    position: absolute; left: 287px; top: 0; width: 3px; height: 100%;
    background: var(--leaf-green);
  }

  .name-band {
    position: absolute; left: 290px; right: 0; top: 52px; height: 58px;
    background: var(--leaf-green);
    padding: 9px 0 0 32px;
    color: var(--paper);
  }
  .person-name { font-size: 25px; line-height: 1; font-weight: 500; letter-spacing: 0.02em; }
  .person-name strong { font-weight: 700; }
  .person-role { font-size: 12px; margin-top: 4px; color: var(--ink-deep); letter-spacing: 0.04em; }

  .contact-list { position: absolute; left: 290px; top: 132px; list-style: none; }
  .contact-item {
    position: relative; display: flex; align-items: center;
    height: 24px; margin-bottom: 11px; padding-left: 48px;
    font-size: 12.5px; color: var(--text-dark);
  }
  .contact-item::before {
    content: ""; position: absolute; left: 4px; top: 6px; width: 20px; height: 12px;
    background: var(--leaf-green);
  }
  .contact-icon {
    position: absolute; left: 16px; top: 0; width: 24px; height: 24px;
    border-radius: 50%; border: 1.5px solid var(--leaf-green); background: var(--paper);
    display: flex; align-items: center; justify-content: center;
  }
  .contact-icon svg { width: 12px; height: 12px; }
  .contact-phone { font-weight: 700; }
  .contact-address { line-height: 1.25; }
</style>
</head>
<body>

<section class="card card-front" aria-label="Business card front">
  <div class="brand"><span class="brand-dot"></span>Bravel Acres</div>
</section>

<section class="card card-back" aria-label="Business card back">
  <div class="back-panel">
    <div class="brand"><span class="brand-dot"></span>Bravel Acres</div>
  </div>
  <div class="divider-rule"></div>

  <div class="name-band">
    <p class="person-name"><strong>DALE</strong> MERRIN</p>
    <p class="person-role">PRESIDENT</p>
  </div>

  <ul class="contact-list">
    <li class="contact-item contact-phone">
      <span class="contact-icon"><svg viewBox="0 0 24 24"><path fill="#1fa9b4" d="M6.6 10.8a15.1 15.1 0 0 0 6.6 6.6l2.2-2.2c.3-.3.7-.4 1-.2 1.1.4 2.3.6 3.6.6.6 0 1 .4 1 1V20c0 .6-.4 1-1 1A17 17 0 0 1 3 4c0-.6.4-1 1-1h3.5c.6 0 1 .4 1 1 0 1.3.2 2.5.6 3.6.1.3 0 .7-.2 1z"/></svg></span>
      731-555-0148
    </li>
    <li class="contact-item">
      <span class="contact-icon"><svg viewBox="0 0 24 24"><rect x="2" y="5" width="20" height="14" rx="1" fill="#1fa9b4"/><path d="M2.5 6l9.5 7 9.5-7" stroke="#fff" stroke-width="1.6" fill="none"/></svg></span>
      bravelacres@mail.com
    </li>
    <li class="contact-item">
      <span class="contact-icon"><svg viewBox="0 0 24 24"><circle cx="12" cy="12" r="10" fill="#1fa9b4"/><path d="M2 12h20M12 2c3 3 3 17 0 20M12 2c-3 3-3 17 0 20" stroke="#fff" stroke-width="1.3" fill="none"/></svg></span>
      www.bravelacres.com
    </li>
    <li class="contact-item contact-address">
      <span class="contact-icon"><svg viewBox="0 0 24 24"><path fill="#1fa9b4" d="M12 2a7 7 0 0 0-7 7c0 5 7 13 7 13s7-8 7-13a7 7 0 0 0-7-7zm0 9.5A2.5 2.5 0 1 1 12 6.5a2.5 2.5 0 0 1 0 5z"/></svg></span>
      2817 W 68th N St<br>Tulsa, OK 74592
    </li>
  </ul>
</section>

</body>
</html>
```